TradeMedic

I want a business card with my logo, a QR code leading to my website, Name, cell number, email, website URL. I am wanting it very clean and up to date. My site colors are black, orange and grey colors. You can look at my homepage for an idea. Information:
Name: Luis Hammond
Cell: 469-587-1942
Email: luis@trademedic.com
www.tradeMedic.com

```html
<!DOCTYPE html>
<html lang="en">
<head>
<meta charset="utf-8">
<title>TradeMedic Business Card</title>
<link rel="stylesheet" href="https://fonts.googleapis.com/css2?family=Montserrat:wght@500;700;800&family=Open+Sans:wght@400;600&display=swap">
<style>
  :root{
    --bg:#d9d9db;
    --card:#ffffff;
    --card-shade:#ececec;
    --ink:#1b1b1b;
    --orange:#ee5a24;
    --grey:#6d6d6d;
  }
  *{margin:0;padding:0;box-sizing:border-box}
  html,body{width:1200px;height:988px;overflow:hidden}
  body{
    background:var(--bg);
    font-family:"Open Sans",sans-serif;
    display:flex;flex-direction:column;align-items:center;justify-content:center;gap:60px;
  }
  .card{
    position:relative;width:700px;height:400px;
    background:linear-gradient(135deg,var(--card) 0%,var(--card) 55%,var(--card-shade) 100%);
    box-shadow:0 10px 30px rgba(0,0,0,.18);
  }
  .wordmark{
    font-family:"Montserrat",sans-serif;font-weight:800;color:var(--ink);
    letter-spacing:-.5px;line-height:1;
  }
  .rule{position:absolute;left:0;right:0;height:3px;background:var(--orange)}
  .rule--top{top:96px}
  .rule--mid{top:262px}
  .rule--bottom{top:352px}
  .card--info .wordmark{position:absolute;left:48px;top:150px;font-size:46px}
  .contacts{
    position:absolute;left:380px;top:122px;width:300px;
    display:grid;grid-template-columns:1fr 1fr;gap:16px 10px;
    font-size:12px;color:var(--grey);
  }
  .contacts .wide{grid-column:1 / span 2}
  .contact{display:flex;align-items:center;gap:7px;white-space:nowrap}
  .contact svg{flex:none;width:18px;height:18px}
  .person{position:absolute;left:48px;top:284px}
  .person__name{font-family:"Montserrat",sans-serif;font-weight:700;font-size:16px;color:var(--orange);letter-spacing:1px;text-transform:uppercase}
  .person__role{font-size:11px;color:var(--grey);letter-spacing:1px;text-transform:uppercase;margin-top:3px}
  .card--logo{display:flex;align-items:center;justify-content:center}
  .card--logo .wordmark{font-size:64px}
</style>
</head>
<body>
  <section class="card card--info">
    <div class="rule rule--top"></div>
    <div class="wordmark">TradeMedic</div>
    <div class="contacts">
      <div class="contact">
        <svg viewBox="0 0 18 18"><circle cx="9" cy="9" r="9" fill="var(--orange)"/><path d="M6 5l2 2-1 1.2a6 6 0 003 3L11.2 10l2 2-1.2 1.2C9 13 5 9 4.8 6.2z" fill="#fff"/></svg>
        469-587-1942
      </div>
      <div class="contact">
        <svg viewBox="0 0 18 18"><circle cx="9" cy="9" r="9" fill="var(--orange)"/><path d="M6 5l2 2-1 1.2a6 6 0 003 3L11.2 10l2 2-1.2 1.2C9 13 5 9 4.8 6.2z" fill="#fff"/></svg>
        469-587-1943
      </div>
      <div class="contact">
        <svg viewBox="0 0 18 18"><circle cx="9" cy="9" r="9" fill="var(--orange)"/><rect x="4.5" y="6" width="9" height="6.5" fill="#fff"/><path d="M4.5 6l4.5 3.5L13.5 6" fill="none" stroke="var(--orange)" stroke-width="1"/></svg>
        luis@trademedic.com
      </div>
      <div class="contact">
        <svg viewBox="0 0 18 18"><circle cx="9" cy="9" r="9" fill="var(--orange)"/><circle cx="9" cy="9" r="4.5" fill="none" stroke="#fff" stroke-width="1.2"/><path d="M4.5 9h9M9 4.5c-2 3-2 6 0 9M9 4.5c2 3 2 6 0 9" fill="none" stroke="#fff" stroke-width="1"/></svg>
        www.tradeMedic.com
      </div>
      <div class="contact wide">
        <svg viewBox="0 0 18 18"><circle cx="9" cy="9" r="9" fill="var(--orange)"/><path d="M9 14s-3.5-3.6-3.5-6a3.5 3.5 0 017 0c0 2.4-3.5 6-3.5 6z" fill="#fff"/><circle cx="9" cy="8" r="1.2" fill="var(--orange)"/></svg>
        12 Harbor Street, Lakeview Road, TX 75001
      </div>
    </div>
    <div class="rule rule--mid"></div>
    <div class="person">
      <div class="person__name">Luis Hammond</div>
      <div class="person__role">Financial Advisor</div>
    </div>
    <div class="rule rule--bottom"></div>
  </section>

  <section class="card card--logo">
    <div class="wordmark">TradeMedic</div>
  </section>
</body>
</html>
```